Construction Company Needs Letterhead Design

We recently had a new logo designed and would like to have our letterhead updated to a trendier design. We are a concrete construction company based out of Iowa, but do work for Agricultural businesses across the Midwest.

Industry/Entity Type

Construction

Colors
ec1f27
000000
ffffff

Requirements
Must have
• Must stay within our current color scheme of red/black/white. Must have have our address, phone number, e-mail address, etc. printed on the letterhead as well.

```html
<!DOCTYPE html>
<html lang="en">
<head>
<meta charset="utf-8">
<title>Brennick Farm Labor Services – Letterhead</title>
<link rel="stylesheet" href="https://fonts.googleapis.com/css2?family=Montserrat:wght@500;600;700;800&family=Arimo:wght@400&display=swap">
<style>
  :root {
    --brand-red: #ec1f27;
    --brand-black: #000000;
    --ink: #222222;
    --paper: #ffffff;
    --backdrop: #ebe8e3;
    --icon-dark: #1d1d1d;
  }
  * { box-sizing: border-box; margin: 0; padding: 0; }
  html, body {
    width: 1200px; height: 1200px; overflow: hidden;
    background: var(--backdrop);
  }
  .letterhead {
    position: absolute; left: 215px; top: 50px;
    width: 770px; height: 1100px;
    background: var(--paper);
    overflow: hidden;
    font-family: "Montserrat", Arial, sans-serif;
    color: var(--ink);
  }
  .brand {
    position: absolute; left: 54px; top: 34px;
    display: flex; align-items: center; gap: 12px;
  }
  .brand-mark {
    width: 46px; height: 46px; background: var(--brand-red);
  }
  .brand-name {
    color: var(--brand-black); font-weight: 800; line-height: 1;
  }
  .brand-name .primary { display: block; font-size: 36px; letter-spacing: 0.5px; }
  .brand-name .secondary { display: block; font-size: 11.5px; letter-spacing: 2.6px; margin-top: 4px; }

  .contact {
    position: absolute; right: 20px; top: 30px;
    list-style: none; text-align: right;
  }
  .contact li {
    display: flex; justify-content: flex-end; align-items: center; gap: 5px;
    color: var(--brand-red); font-weight: 600; font-size: 13.5px; line-height: 16px;
  }
  .contact-icon { width: 11px; height: 11px; flex: none; }

  .recipient {
    position: absolute; left: 52px; top: 206px;
    font-weight: 500; font-size: 16.5px; line-height: 20px; color: #2a2a2a;
  }
  .recipient p { margin-bottom: 17px; }
  .recipient .address-block { margin-top: 21px; }

  .letter-body {
    position: absolute; left: 67px; top: 394px; width: 640px;
    font-family: "Arimo", Arial, sans-serif; font-size: 10.4px; line-height: 12.4px;
    color: #333333;
  }
  .letter-body p { margin-bottom: 12px; }

  .closing {
    position: absolute; right: 50px; top: 904px;
    font-weight: 700; font-size: 16px; color: #2a2a2a;
  }
  .signature {
    display: block; margin: 6px 0 0 30px; width: 70px; height: 12px;
    background: linear-gradient(90deg, #c9c9c9, #e4e4e4);
    border-radius: 6px;
  }
  .footer-wave {
    position: absolute; left: 0; bottom: 0; width: 770px; height: 110px;
  }
</style>
</head>
<body>
  <main class="letterhead">
    <header>
      <div class="brand">
        <span class="brand-mark"></span>
        <span class="brand-name">
          <span class="primary">BRENNICK</span>
          <span class="secondary">FARM LABOR SERVICES</span>
        </span>
      </div>
      <ul class="contact">
        <li>4720 County Road K-12
          <svg class="contact-icon" viewBox="0 0 12 12"><circle cx="6" cy="6" r="6" fill="var(--icon-dark)"/><path d="M6 2.6a2.2 2.2 0 0 0-2.2 2.2C3.8 6.6 6 9.4 6 9.4s2.2-2.8 2.2-4.6A2.2 2.2 0 0 0 6 2.6z" fill="#fff"/><circle cx="6" cy="4.8" r="0.8" fill="var(--icon-dark)"/></svg>
        </li>
        <li>Marlow, Iowa 50412</li>
        <li>(515) 555-0142
          <svg class="contact-icon" viewBox="0 0 12 12"><circle cx="6" cy="6" r="6" fill="var(--icon-dark)"/><path d="M4.2 3c.3 0 .5.1.6.4l.4 1c.1.2 0 .4-.1.6l-.4.4c.3.7.9 1.3 1.6 1.6l.4-.4c.2-.2.4-.2.6-.1l1 .4c.3.1.4.3.4.6v.6c0 .4-.3.7-.7.7C5.5 8.8 3.2 6.5 3.2 4.1c0-.4.3-.7.7-.7z" fill="#fff"/></svg>
        </li>
        <li>(515) 555-0187
          <svg class="contact-icon" viewBox="0 0 12 12"><circle cx="6" cy="6" r="6" fill="var(--icon-dark)"/><rect x="3.6" y="2.8" width="4.8" height="2.2" fill="#fff"/><rect x="3" y="5.2" width="6" height="3.4" rx="0.6" fill="#fff"/><rect x="4.2" y="6.8" width="3.6" height="0.8" fill="var(--icon-dark)"/></svg>
        </li>
      </ul>
    </header>

    <section class="recipient">
      <p>Date</p>
      <p>Recipent Name</p>
      <div class="address-block">
        <div>Company Name</div>
        <div>Street Address</div>
        <div>City,State,Zip</div>
      </div>
    </section>

    <section class="letter-body">
      <p>Lorem ipsum dolor sit amet, consectetur adipiscing elit. Fusce rutrum mi mi, vel lobortis lorem auctor vel. Fusce eu elit sit amet tortor semper ultrices. Mauris varius nulla justo, sed condimentum nisl rutrum ut. Nunc nec fermentum tortor, et vehicula tortor. Aliquam ultrices purus velit, vitae scelerisque massa efficitur vitae. Integer mollis risus neque. Donec accumsan, arcu ut porttitor pellentesque, turpis orci bibendum ante, vitae sodales urna dolor vel ligula. Phasellus sit amet aliquet est.</p>
      <p>Praesent eu ullamcorper justo, quis pellentesque velit. Donec accumsan, sem at consequat efficitur, orci nunc dignissim purus, nec molestie lorem risus quis metus. Fusce et justo placerat, tempus mi vel, congue justo. Pellentesque sodales odio nisl, at pretium neque rutrum quis. Etiam scelerisque metus vitae porta vehicula. Fusce dignissim mollis bibendum. Duis tincidunt sem mauris, malesuada cursus quam suscipit in. Curabitur bibendum leo leo. Pellentesque quis tellus eget erat auctor euismod eu a odio. Duis a eros dolor. Quisque non nunc sed velit dictum eleifend. Nunc semper dapibus orci nec dapibus. Aenean a dignissim leo. Proin dictum et lectus et commodo. Cras hendrerit ex id lectus sodales bibendum.</p>
      <p>Vivamus at erat purus. Nunc lacus risus, egestas sed gravida a, egestas nec elit. Vestibulum pharetra dolor tempor ex ornare vehicula ac sodales libero. In eu vehicula orci, in aliquam ex. Praesent vulputate ex egestas tortor maximus porta. Aliquam in elit vitae tellus pulvinar porttitor. Morbi quis turpis nunc. Nam sodales magna purus, a eleifend dui maximus a. Nunc lobortis, mi pellentesque bibendum aliquam, dolor lectus iaculis nibh, at finibus elit lorem non erat. Nunc lectus mauris, suscipit quis fringilla at, eleifend sed leo. Nullam porttitor eros id elementum sagittis.</p>
      <p>Proin tincidunt finibus fermentum. Ut pulvinar, neque eu rutrum ornare, magna ex bibendum mauris, quis egestas ligula velit in justo. Praesent fringilla dapibus leo. Suspendisse mollis, mauris rhoncus lobortis tincidunt, lectus dolor sodales nulla, eu convallis ipsum nunc at quam. Aenean leo arcu, suscipit sit amet porttitor vel, molestie sit amet odio. Aliquam blandit odio urna, sit amet imperdiet augue lacinia a. Fusce aliquam orci id libero auctor, quis feugiat purus gravida. Ut luctus orci vitae euismod sollicitudin. Fusce porta auctor metus, vel mollis urna pretium ut. Nunc pellentesque quis urna in ultricies. Nulla gravida purus facilisis, iaculis dui tempor, sagittis elit. Mauris justo nulla, faucibus feugiat egestas ac, viverra eget dui. Vestibulum suscipit ex venenatis, aliquam nibh et, commodo odio.</p>
      <p>Phasellus at ligula gravida lacus viverra egestas. Fusce sagittis a eros ut mattis. Morbi molestie urna orci, in porttitor lectus malesuada nec. Maecenas vulputate lacus a tortor posuere facilisis. Maecenas non tempor sem. Suspendisse at aliquet nisi, vel dignissim metus. Donec magna quam, pulvinar sed pharetra quis, consequat ac ante.</p>
    </section>

    <div class="closing">
      Sincerely Yours,
      <span class="signature" role="img" aria-label="Handwritten signature"></span>
    </div>

    <svg class="footer-wave" viewBox="0 0 770 110" preserveAspectRatio="none" aria-hidden="true">
      <path d="M0 62 C180 32 420 22 660 26 C520 34 260 56 0 94 Z" fill="var(--brand-black)"/>
      <path d="M0 110 L0 102 C250 64 520 44 770 38 L770 110 Z" fill="var(--brand-red)"/>
    </svg>
  </main>
</body>
</html>
```